Business Card - Professional Minimalist - Double sided

We appreciate minimalist logo/web/collateral designs that allow design to tell a story. We want to relay a professional image/approach but throwing in a splash of modern when we’re able so long as it’s not distracting. Think 75% classic corporate, 25% modern. Open to black or white design, not sure which might look the best.

Target Market(s)

Senior executives or related government affairs contacts within the agriculture, energy, and defense industries (i.e., potential clients) but located outside of Washington, DC. Most potential clients based in DC with be familiar with both of us and our shared history.

Industry/Entity Type

Consulting

Contact Information for Business Card

Name: Daniel R. Whitlock
Title: Co-Founder & Partner
Address: 418 Bramblewood Ave. SE | Suite 2716 | Washington, D.C. 20019
Phone: (202) 555-0187
Email: Daniel@HollerbyWhitlock.com

Font styles to use
Serif

Colors

Designer to choose only greyscale colors for use in the design.

Requirements
Must have
• Name: Daniel R. Whitlock
Phone: (202) 555-0187

```html
<!DOCTYPE html>
<html lang="en">
<head>
<meta charset="utf-8">
<title>Hollerby Whitlock Group – Business Card</title>
<link rel="stylesheet" href="https://fonts.googleapis.com/css2?family=Arimo:wght@400;700&family=Cinzel:wght@400&display=swap">
<style>
  :root {
    --page-bg: #e4e4e2;
    --card-white: #ffffff;
    --card-shade: #f1f1f1;
    --band-dark: #4d4d4d;
    --band-light: #a9a9a9;
    --ink-strong: #4a4a4a;
    --ink-soft: #5e5e5e;
    --rule: #b5b5b5;
  }
  * { margin: 0; padding: 0; box-sizing: border-box; }
  html, body {
    width: 1200px; height: 900px; overflow: hidden;
    background: var(--page-bg);
  }
  .canvas {
    width: 1200px; height: 900px;
    display: flex; flex-direction: column;
    align-items: center; justify-content: center; gap: 50px;
  }
  .card {
    position: relative;
    width: 630px; height: 360px;
    background: linear-gradient(180deg, var(--card-white) 55%, var(--card-shade));
    box-shadow: 0 6px 18px rgba(0,0,0,0.12);
    overflow: hidden;
  }
  .card__band-top {
    position: absolute; top: 0; left: 0; right: 0;
    height: 12px; background: var(--band-dark);
  }
  .card__band-bottom {
    position: absolute; bottom: 0; left: 0; right: 0;
    height: 18px; background: var(--band-light);
  }

  /* Front */
  .brand {
    position: absolute; inset: 12px 0 18px 0;
    display: flex; align-items: center; justify-content: center; gap: 14px;
  }
  .brand__mark {
    width: 30px; height: 30px;
    background: var(--band-dark);
  }
  .brand__name {
    font-family: "Cinzel", "Times New Roman", serif;
    font-weight: 400; font-size: 27px; letter-spacing: 1px;
    color: var(--ink-strong);
  }

  /* Back */
  .contact {
    position: absolute; inset: 12px 0 18px 0;
    display: flex; flex-direction: column; align-items: center;
    font-family: "Arimo", Arial, sans-serif; color: var(--ink-soft);
    text-align: center;
  }
  .contact__name {
    margin-top: 62px;
    font-weight: 700; font-size: 24px; color: var(--ink-strong);
  }
  .contact__title { margin-top: 4px; font-size: 14px; }
  .contact__rule {
    width: 330px; height: 1px; background: var(--rule);
    margin-top: 30px;
  }
  .contact__line { font-size: 15px; margin-top: 40px; }
  .contact__line + .contact__line { margin-top: 22px; }
</style>
</head>
<body>
<main class="canvas">
  <section class="card card--front" aria-label="Card front">
    <div class="card__band-top"></div>
    <div class="brand">
      <span class="brand__mark"></span>
      <span class="brand__name">Hollerby Whitlock Group</span>
    </div>
    <div class="card__band-bottom"></div>
  </section>

  <section class="card card--back" aria-label="Card back">
    <div class="card__band-top"></div>
    <div class="contact">
      <p class="contact__name">Daniel R. Whitlock</p>
      <p class="contact__title">Co-Founder &amp; Partner</p>
      <div class="contact__rule"></div>
      <p class="contact__line">P: (202) 555-0187 &nbsp;|&nbsp; E: Daniel@HollerbyWhitlock.com</p>
      <p class="contact__line">418 Bramblewood Ave. SE &nbsp;|&nbsp; Suite 2716 &nbsp;|&nbsp; Washington, D.C. 20019</p>
    </div>
    <div class="card__band-bottom"></div>
  </section>
</main>
</body>
</html>
```